Brookfarrow Osteopathy and dry needling business card

Business card for Brookfarrow Osteopathy and Dry Needling.

Industry/Entity Type

Health

Contact Information for Business Card

I do not have a phone number yet. I also do not have an email address yet. The physical address is: 48 Lower Crane Street Brookfarrow The website is: www.brookfarrowosteosteopathy.example My details are: Dr Martin Pellowe, Osteopath (B.Clin.Sci (Ost) M.Ost BSC ECON (Hons)

Colors
0094D4
00A9DD
6FCCEA
C7EBF8
E9F6FB

Requirements
Must have
• logo on the back
Nice to have
• Maybe a space for me to write an appointment time and date on the card.

```html
<!DOCTYPE html>
<html lang="en">
<head>
<meta charset="utf-8">
<title>Brookfarrow Osteopathy and Dry Needling – Business Card</title>
<link rel="stylesheet" href="https://fonts.googleapis.com/css2?family=Outfit:wght@400;500;700&display=swap">
<style>
  :root {
    --backdrop: #a7a7a7;
    --orange: #f68d2b;
    --orange-deep: #c0692a;
    --brown: #4a2f1e;
    --blue: #0094d4;
    --blue-dark: #1d2733;
    --ink-blue: #0e6f98;
    --white: #ffffff;
  }
  * { box-sizing: border-box; margin: 0; padding: 0; }
  html, body {
    width: 1200px; height: 1200px; overflow: hidden;
    background: var(--backdrop);
    font-family: "Outfit", Arial, sans-serif;
  }
  .card {
    position: absolute;
    left: 141px;
    width: 918px;
    height: 523px;
    overflow: hidden;
    box-shadow: 8px 10px 14px rgba(0,0,0,0.28);
  }
  .card--front {
    top: 51px;
    background: linear-gradient(120deg, var(--brown) 0%, var(--orange-deep) 45%, var(--orange) 100%);
  }
  .card--back {
    top: 624px;
    background: var(--orange);
  }
  .front-wave { position: absolute; inset: 0; width: 100%; height: 100%; }
  .holder {
    position: absolute; left: 62px; top: 254px; color: var(--white);
  }
  .holder__name { font-size: 40px; font-weight: 700; letter-spacing: 0.2px; line-height: 1; }
  .holder__title { margin-top: 16px; font-size: 18px; font-weight: 400; }
  .contact {
    position: absolute; left: 62px; top: 399px; list-style: none; color: var(--white);
    font-size: 22px; font-weight: 400;
  }
  .contact__item { display: flex; align-items: center; height: 37px; }
  .contact__icon { width: 20px; height: 20px; margin-right: 23px; flex: none; }
  .brand-mark {
    position: absolute;
    display: flex; align-items: center; justify-content: center; text-align: center;
    border-radius: 50%;
    font-weight: 500; text-transform: uppercase; line-height: 1.25;
  }
  .brand-mark--front {
    left: 628px; top: 72px; width: 224px; height: 224px;
    border: 3px solid var(--white); color: var(--white); font-size: 18px; padding: 22px;
  }
  .brand-mark--back {
    left: 316px; top: 134px; width: 254px; height: 254px;
    border: 3px solid var(--ink-blue); color: var(--ink-blue); font-size: 21px; padding: 24px;
  }
</style>
</head>
<body>
  <section class="card card--front" aria-label="Business card front">
    <svg class="front-wave" viewBox="0 0 918 523" aria-hidden="true">
      <defs>
        <linearGradient id="waveBlue" x1="0" y1="0" x2="1" y2="0">
          <stop offset="0" stop-color="var(--blue)"/>
          <stop offset="1" stop-color="var(--blue-dark)"/>
        </linearGradient>
      </defs>
      <path d="M0,190 C200,120 380,88 580,90 C555,190 610,300 740,330 C800,343 850,336 905,318 C885,410 850,470 800,523 L0,523 Z"
            fill="url(#waveBlue)" stroke="var(--white)" stroke-width="14" stroke-linejoin="round"/>
      <path d="M0,190 C200,120 380,88 580,90 C555,190 610,300 740,330 C800,343 850,336 905,318 C885,410 850,470 800,523 L0,523 Z"
            fill="url(#waveBlue)"/>
    </svg>

    <div class="brand-mark brand-mark--front">Brookfarrow Osteopathy and Dry Needling</div>

    <div class="holder">
      <h1 class="holder__name">Dr Martin Pellowe</h1>
      <p class="holder__title">Osteopath (B.Clin.Sci (Ost) M.Ost BSC ECON (Hons)</p>
    </div>

    <ul class="contact">
      <li class="contact__item">
        <svg class="contact__icon" viewBox="0 0 20 20" aria-hidden="true">
          <path d="M10 1.5a6 6 0 0 0-6 6c0 4.5 6 11 6 11s6-6.5 6-11a6 6 0 0 0-6-6z" fill="var(--white)"/>
          <circle cx="10" cy="7.5" r="2.2" fill="#1475a5"/>
        </svg>
        48 Lower Crane Street Brookfarrow
      </li>
      <li class="contact__item">
        <svg class="contact__icon" viewBox="0 0 20 20" aria-hidden="true">
          <circle cx="10" cy="10" r="8.5" fill="var(--white)"/>
          <ellipse cx="10" cy="10" rx="3.6" ry="8.5" fill="none" stroke="#136f9c" stroke-width="1.4"/>
          <line x1="1.5" y1="10" x2="18.5" y2="10" stroke="#136f9c" stroke-width="1.4"/>
        </svg>
        www.brookfarrowosteosteopathy.example
      </li>
    </ul>
  </section>

  <section class="card card--back" aria-label="Business card back">
    <div class="brand-mark brand-mark--back">Brookfarrow Osteopathy and Dry Needling</div>
  </section>
</body>
</html>
```